Web design for business website

I need a web design for a business website for one of our clients who is specialized in alarm management software. I would like you to design 3 web pages, one for each of the 3 pages. You need to process the corporate identity of our client to the web design. This means the colors of the logo (red and black) should definitely show up on all of the 3 pages. Find the logo file for the logo of our customer. To increase readability I suggest you use a white/light background. All suggestions are welcome.

Please kindly download atttached Webdesign.zip and read the project brief first. The project brief refers to all other files of the zip file. Your design must have exactly the same structure as the wireframes.
Updates

Target Market(s)

B2B, Alarm management

Industry/Entity Type

Business

Number of Pages Required

3 page

Requirements
Must have
• The web design must have exactly the same structure as the wireframes and needs to contain the colors of the company logo.

```html
<!DOCTYPE html>
<html lang="en">
<head>
<meta charset="utf-8">
<title>Kalvion – Real-time reasoning solutions</title>
<link href="https://fonts.googleapis.com/css2?family=Montserrat:wght@700&family=Open+Sans:ital,wght@0,400;0,600;1,400&display=swap" rel="stylesheet">
<style>
:root{
  --brand:#e8430f;
  --ink:#1e1c3a;
  --text:#555;
  --muted:#777;
  --line:#e2e2e2;
  --sky:#e4eff8;
  --panel:#edf4fa;
  --tile:#d6e9f1;
}
*{box-sizing:border-box;margin:0;padding:0}
html,body{width:759px;height:1200px;overflow:hidden;background:#fff}
body{font-family:"Open Sans",sans-serif;color:var(--text);position:relative}
.abs{position:absolute}
.topbar{left:0;top:0;width:759px;height:35px;background:#f3f7fa}
.topbar .phone{left:34px;top:9px;font-size:10px;color:#555;display:flex;align-items:center;gap:8px}
.lang{left:478px;top:12px;font-size:9px;color:#444;display:flex;align-items:center;gap:5px}
.flag{width:11px;height:8px;background:#c7d2e6;display:inline-block}
.search{left:560px;top:7px;width:165px;height:22px;border:1px solid #cfcfcf;background:#fff;font-size:8.5px;font-style:italic;color:#777;padding:5px 12px}
.search .go{position:absolute;right:-1px;top:-1px;width:22px;height:22px;background:var(--brand);display:flex;align-items:center;justify-content:center}
.header{left:0;top:35px;width:759px;height:103px;background:#f8fafc}
.logo-dot{left:34px;top:63px;width:47px;height:47px;border-radius:50%;background:var(--brand)}
.brand{left:95px;top:60px;font-family:"Montserrat",sans-serif;font-weight:700;font-size:33px;letter-spacing:2px;color:var(--ink)}
.tagline{left:95px;top:98px;font-size:10.5px;color:var(--ink)}
.userbtn{top:65px;height:36px;background:var(--tile);font-size:7.5px;color:#555;display:flex;flex-direction:column;align-items:center;justify-content:center;gap:3px}
.nav{left:0;top:138px;width:759px;height:34px;background:var(--brand);display:flex;align-items:center;font-size:11.5px;color:#fff;text-transform:uppercase}
.nav span{position:absolute}
.nav .active{color:var(--ink);font-weight:600}
.hero{left:0;top:172px;width:759px;height:341px;background:linear-gradient(180deg,#6f7a82 0%,#c9b790 30%,#e8b055 48%,#8a8f6a 64%,#4f6a3a 78%,#5c5a48 100%)}
.section-title{left:0;width:759px;text-align:center;color:var(--brand);font-size:14.5px;font-weight:600}
.rule{left:310px;width:140px;height:3px;border-top:1px solid var(--line);border-bottom:1px solid var(--line)}
.intro{left:50px;top:586px;width:659px;text-align:center;font-size:8.9px;line-height:15.2px;color:var(--muted)}
.more{left:368px;top:691px;width:25px;height:25px;border-radius:50%;background:var(--brand);display:flex;align-items:center;justify-content:center}
.divider{left:34px;top:737px;width:691px;height:1px;background:var(--line)}
.clients{left:43px;top:802px;width:672px;height:88px;border:1px solid #e3e3e3;background:#fff}
.client{top:836px;font-size:13px;font-weight:600;color:#555}
.footer{left:0;top:925px;width:759px;height:275px;background:var(--sky)}
.social{top:946px;width:24px;height:24px;border-radius:50%;border:1px solid #aaa}
.social.on{background:var(--brand);border-color:var(--brand)}
.nl-label{left:435px;top:953px;font-size:11.5px;font-weight:600;color:var(--brand)}
.nl-input{left:513px;top:947px;width:180px;height:26px;background:#fff;border:1px solid #d7dde2;font-size:11px;color:#666;padding:5px 9px}
.nl-send{left:693px;top:947px;width:32px;height:26px;background:var(--brand);display:flex;align-items:center;justify-content:center}
.panel{left:34px;top:995px;width:691px;height:165px;background:var(--panel)}
.col h4{font-size:11px;font-weight:600;color:var(--brand);text-transform:uppercase;padding-bottom:6px;border-bottom:1px solid #c9d3da;display:inline-block}
.col ul{list-style:none;margin-top:10px}
.col li{font-size:8.8px;color:#666;height:23px;display:flex;align-items:center;gap:9px}
.col li::before{content:"";width:5px;height:5px;border:1px solid #999;display:inline-block}
.col li.current{color:var(--brand)}
.col li.current::before{border-color:var(--brand)}
.contact{font-size:8.8px;color:#555;line-height:13px;display:flex;gap:10px;align-items:flex-start}
.copy{left:0;top:1176px;width:759px;text-align:center;font-size:8.8px;color:#777}
</style>
</head>
<body>
<div class="abs topbar"></div>
<div class="abs phone topbar-phone" style="left:34px;top:9px;font-size:10px;display:flex;align-items:center;gap:8px">
  <svg width="17" height="17" viewBox="0 0 17 17"><circle cx="8.5" cy="8.5" r="7.5" fill="none" stroke="#333" stroke-width="1.2"/><path d="M6 5l1.5 1.5-1 1c.5 1 1.5 2 2.5 2.5l1-1L11.5 10.5 10.5 11.8C8 11.5 5.5 9 5.2 6.5z" fill="#333"/></svg>
  <span>+31 (0)20 5550 184</span>
</div>
<div class="abs lang"><span class="flag"></span>ENGLISH <svg width="6" height="4"><path d="M0 0h6L3 4z" fill="#444"/></svg></div>
<div class="abs search">Search....<span class="go"><svg width="11" height="11" viewBox="0 0 11 11"><circle cx="6.5" cy="4.5" r="3.3" fill="none" stroke="#fff" stroke-width="1.4"/><path d="M4 7L1 10" stroke="#fff" stroke-width="1.6"/></svg></span></div>

<header class="abs header"></header>
<div class="abs logo-dot"></div>
<div class="abs brand">KALVION</div>
<div class="abs tagline">Real-time reasoning solutions</div>
<div class="abs userbtn" style="left:590px;width:40px">
  <svg width="11" height="11" viewBox="0 0 11 11"><circle cx="5.5" cy="3" r="2.6" fill="#666"/><path d="M0 11c0-4 11-4 11 0z" fill="#666"/></svg>Account</div>
<div class="abs userbtn" style="left:638px;width:40px">
  <svg width="9" height="11" viewBox="0 0 9 11"><path d="M2 5V3.3a2.5 2.5 0 015 0V5" fill="none" stroke="#666" stroke-width="1.3"/><rect y="5" width="9" height="6" fill="#666"/></svg>Login</div>
<div class="abs userbtn" style="left:685px;width:40px">
  <svg width="12" height="11" viewBox="0 0 12 11"><circle cx="5" cy="3" r="2.6" fill="#666"/><path d="M0 11c0-4 10-4 10 0z" fill="#666"/><path d="M10 5v4M8 7h4" stroke="#666" stroke-width="1.2"/></svg>Sing up</div>

<nav class="abs nav">
  <span class="active" style="left:40px">Home</span>
  <span style="left:119px">Industry</span>
  <span style="left:219px">Telecom</span>
  <span style="left:316px">Power</span>
  <span style="left:401px">Utilties</span>
  <span style="left:492px">Infra</span>
  <span style="left:570px">Store</span>
  <span style="left:651px">Contact us</span>
</nav>

<div class="abs hero" role="img" aria-label="Photograph of an industrial refinery at sunset behind a marsh with tall grass"></div>

<h2 class="abs section-title" style="top:543px">WELCOME TO KALVION</h2>
<div class="abs rule" style="top:572px"></div>
<p class="abs intro">Companies have invested to get data out of processes. New technologies have been developed to get real-time data out of the harshest places, like oil-well drill heads or the Great Barrier Riff. Data in itself means nothing without the context the data is collected in. Example: data from equipment under maintenance does not provide information to operations. Information - data which is valid and meaningful - can overwhelm any user without the proper knowledge to interpret this information. Kalvion technology enables easy application of such knowledge in a comprehensible – visual – representation and makes hypothetical reasoning with information possible providing meaningful advisories to subscribers when they need it or when it is required that they are made aware of a situation which requires their attention.</p>
<div class="abs more"><svg width="10" height="12" viewBox="0 0 10 12"><path d="M2 1l5 5-5 5" fill="none" stroke="#fff" stroke-width="2.4"/></svg></div>
<div class="abs divider"></div>

<h2 class="abs section-title" style="top:754px">CLIENTS</h2>
<div class="abs rule" style="top:783px"></div>
<div class="abs clients"></div>
<svg class="abs" style="left:34px;top:832px" width="24" height="30" viewBox="0 0 24 30"><path d="M22 0L2 15l20 15-10-15z" fill="var(--brand)"/></svg>
<svg class="abs" style="left:702px;top:832px" width="24" height="30" viewBox="0 0 24 30"><path d="M2 0l20 15-20 15 10-15z" fill="#ddd"/></svg>
<span class="abs client" style="left:68px">Norvel</span>
<span class="abs client" style="left:132px">Orvida</span>
<span class="abs client" style="left:212px">Brauwen</span>
<span class="abs client" style="left:346px">Tessaport</span>
<span class="abs client" style="left:472px">Kestrel Oil</span>
<span class="abs client" style="left:575px">Corvane</span>
<span class="abs client" style="left:645px">Almiro</span>

<footer class="abs footer"></footer>
<div class="abs social on" style="left:35px"></div>
<div class="abs social" style="left:64px"></div>
<div class="abs social" style="left:92px"></div>
<div class="abs social" style="left:121px"></div>
<div class="abs social" style="left:150px"></div>
<div class="abs social" style="left:178px"></div>
<div class="abs nl-label">NEWSLETTER</div>
<div class="abs nl-input">@email_address</div>
<div class="abs nl-send"><svg width="16" height="14" viewBox="0 0 16 14"><path d="M0 6L16 0 12 14 8 9z" fill="#fff"/><path d="M8 9L16 0" stroke="var(--brand)" stroke-width="1"/></svg></div>

<div class="abs panel"></div>
<div class="abs col" style="left:48px;top:1012px">
  <h4>Solutions</h4>
  <ul><li class="current">KAM Alarm Reporting</li><li>KAM Alarm Analysis</li><li>KAM Alarm Expert</li><li>Use</li></ul>
</div>
<div class="abs col" style="left:197px;top:1012px">
  <h4>Industries</h4>
  <ul><li>Industry</li><li>Telceom</li><li>Power</li><li>Infra</li></ul>
</div>
<div class="abs col" style="left:320px;top:1012px">
  <h4>About us</h4>
  <ul><li>Compnay</li><li>Overview</li><li>Leadership</li><li>Partners</li><li>Locations</li></ul>
</div>
<div class="abs col" style="left:436px;top:1012px">
  <h4>News</h4>
  <ul><li>Product News</li><li>Partner News</li><li>Events</li><li>Press Releases</li><li>Vacancies</li></ul>
</div>
<div class="abs col" style="left:546px;top:1012px">
  <h4>Contacts Informations</h4>
</div>
<div class="abs contact" style="left:554px;top:1045px">
  <svg width="20" height="22" viewBox="0 0 20 22"><rect x="8" y="0" width="3" height="22" fill="var(--brand)"/><path d="M2 3h15l3 3-3 3H2z" fill="var(--brand)"/><path d="M18 11H5l-3 3 3 3h13z" fill="var(--brand)"/></svg>
  <span>Kalvion Suite 4, Lorem econse<br>Post Box 518 NEWPORT 5821</span>
</div>
<div class="abs contact" style="left:555px;top:1090px;align-items:center">
  <svg width="18" height="18" viewBox="0 0 18 18"><path d="M3 1l3 4-2 2c1 3 3 5 6 6l2-2 4 3-2 3C7 17 1 11 1 3z" fill="var(--brand)"/></svg>
  <span>31 (0)20 5550 184</span>
</div>
<div class="abs contact" style="left:554px;top:1128px;align-items:center">
  <svg width="20" height="14" viewBox="0 0 20 14"><rect width="20" height="14" fill="var(--brand)"/><path d="M0 0l10 8 10-8" fill="none" stroke="#fff" stroke-width="1.2"/></svg>
  <span>info@kalvion.com</span>
</div>

<div class="abs copy">Copyright © 2015 kalvion com | All Rights Reserved.</div>
</body>
</html>
```